Promotional business a5 Notepad design

I am looking for a custom a5 notepad design as a promotional item to give away to customers etc.
Attached will be a desk planner we had designed feel free to use as a reference.
We want the notepad to have lines running horizontal not squares like the desk planner example.

Industry/Entity Type

Hydraulic / industrial

Colors

Designer to choose colors to be used in the design.

```html
<!DOCTYPE html>
<html lang="en">
<head>
<meta charset="utf-8">
<title>Corvane Hose and Fittings – Notepad</title>
<link rel="stylesheet" href="https://fonts.googleapis.com/css2?family=Poppins:ital,wght@0,400;0,700;1,800&display=swap">
<style>
  :root {
    --brand-blue: #2a4a9c;
    --brand-yellow: #f6c318;
    --footer-dark: #1b1b1b;
    --rule-grey: #a3a3a3;
    --paper: #ffffff;
    --ink-light: #ffffff;
  }
  * { margin: 0; padding: 0; box-sizing: border-box; }
  html, body { width: 849px; height: 1200px; overflow: hidden; background: var(--paper); }
  .notepad {
    position: relative;
    width: 849px;
    height: 1200px;
    background: var(--paper);
    font-family: "Poppins", sans-serif;
  }
  .header {
    position: absolute;
    left: 0; top: 0;
    width: 849px; height: 178px;
    background: var(--brand-blue);
    border-bottom: 6px solid var(--brand-yellow);
    height: 184px;
  }
  .brand-card {
    position: absolute;
    left: 62px; top: 38px;
    width: 353px; height: 106px;
    background: var(--paper);
    border-radius: 14px;
    display: flex;
    align-items: center;
    justify-content: center;
    gap: 12px;
  }
  .brand-dot {
    width: 34px; height: 34px;
    border-radius: 50%;
    background: var(--brand-blue);
    flex: none;
  }
  .brand-name {
    font-weight: 700;
    font-size: 21px;
    line-height: 1.1;
    color: var(--brand-blue);
    text-transform: uppercase;
    letter-spacing: 0.5px;
  }
  .tagline {
    position: absolute;
    right: 59px; top: 40px;
    text-align: right;
    color: var(--brand-yellow);
    font-weight: 800;
    font-style: italic;
    font-size: 27px;
    line-height: 34.5px;
  }
  .writing-lines {
    position: absolute;
    left: 56px; top: 229.5px;
    width: 736px;
  }
  .writing-lines span {
    display: block;
    height: 36.26px;
    border-top: 1px solid var(--rule-grey);
  }
  .writing-lines span:last-child { height: 1px; }
  .footer {
    position: absolute;
    left: 0; bottom: 0;
    width: 849px; height: 88px;
    background: var(--footer-dark);
    border-top: 6px solid var(--brand-yellow);
    color: var(--ink-light);
    font-size: 14.5px;
    line-height: 22px;
    letter-spacing: 0.6px;
    text-transform: uppercase;
  }
  .service-area {
    position: absolute;
    left: 60px; top: 22px;
    display: flex;
    gap: 14px;
  }
  .service-area svg { margin-top: 4px; }
  .contact {
    position: absolute;
    right: 44px; top: 22px;
    text-align: right;
  }
  .contact-row { display: flex; justify-content: flex-end; align-items: center; gap: 12px; }
  .contact-row svg { flex: none; }
</style>
</head>
<body>
<main class="notepad">
  <header class="header">
    <div class="brand-card">
      <span class="brand-dot"></span>
      <span class="brand-name">Corvane<br>Hose and Fittings</span>
    </div>
    <p class="tagline">Industry Chosen<br>Hose And Fittings<br>Provider</p>
  </header>

  <section class="writing-lines" aria-label="Writing lines">
    <span></span><span></span><span></span><span></span><span></span><span></span>
    <span></span><span></span><span></span><span></span><span></span><span></span>
    <span></span><span></span><span></span><span></span><span></span><span></span>
    <span></span><span></span><span></span><span></span><span></span><span></span>
  </section>

  <footer class="footer">
    <div class="service-area">
      <svg width="14" height="18" viewBox="0 0 14 18" aria-hidden="true">
        <path d="M7 0C3.1 0 0 3.1 0 7c0 5 7 11 7 11s7-6 7-11c0-3.9-3.1-7-7-7z" fill="#fff"/>
        <circle cx="7" cy="7" r="2.8" fill="#1b1b1b"/>
      </svg>
      <p>Servicing the Harbourton<br>Metropolitan Area</p>
    </div>
    <div class="contact">
      <div class="contact-row">
        <span>Email@corvanehose.com.au</span>
        <svg width="16" height="12" viewBox="0 0 16 12" aria-hidden="true">
          <rect width="16" height="12" rx="1.5" fill="#fff"/>
          <path d="M1 1.5l7 5.5 7-5.5" stroke="#1b1b1b" stroke-width="1.6" fill="none"/>
        </svg>
      </div>
      <div class="contact-row">
        <span>General Enquiries: 08 5550 1427</span>
        <svg width="17" height="14" viewBox="0 0 17 14" aria-hidden="true">
          <path d="M1 4.5C1 2 4.5 1 8.5 1S16 2 16 4.5v1.2h-3.6V3.9H4.6v1.8H1z" fill="#fff"/>
          <path d="M3 13l1.6-6h7.8L14 13z" fill="#fff"/>
          <circle cx="8.5" cy="9.5" r="1.6" fill="#1b1b1b"/>
        </svg>
      </div>
    </div>
  </footer>
</main>
</body>
</html>
```